Pediatric Occupational Therapy Brochure Design

This design really needs to stand out, especially with all the wordage that I have included. These brochures will be given to doctors, future clients, and caregivers. I have included the logo on by brochure, so incorporating the same or similar colors would be fantastic. A trifold brochure would probably be best to fit all the information, as this is a new business and needs to convey all the information in a way that people will read.

Target Market(s)

Doctor's offices and caregivers of children with disabilities.

Industry/Entity Type

Health Care

Font styles to use
Serif
Sans Serif

Colors
33a6d7
85acd3
ffffff
33b8a4
86cfc7

Requirements
Must have
• I would like the same colors of the logo incorporated in the brochure design.
Nice to have
• I would like to see the butterfly somehow in the background or used in the design. Also a trifold or two page design would be greatly appreciated as long as the information can fit.

```html
<!DOCTYPE html>
<html lang="en">
<head>
<meta charset="utf-8">
<title>Kite Kids Therapy — Trifold Brochure</title>
<link rel="stylesheet" href="https://fonts.googleapis.com/css2?family=Roboto:wght@300;400;500&display=swap">
<style>
  :root {
    --blue: #33a6d7;
    --teal: #33b8a4;
    --teal-soft: #86cfc7;
    --sky: #85acd3;
    --white: #ffffff;
    --ink: #555a5e;
    --ink-dark: #3f4347;
    --fold: #e4e5e6;
    --stage: #dcdddf;
  }
  * { box-sizing: border-box; margin: 0; padding: 0; }
  html, body {
    width: 1200px; height: 1072px; overflow: hidden;
    background: var(--stage);
    font-family: "Roboto", Arial, sans-serif;
    color: var(--ink);
  }
  .brochure {
    position: absolute; left: 30px; top: 130px;
    width: 1140px; height: 811px;
    background: var(--white);
    box-shadow: 0 6px 24px rgba(0,0,0,0.18);
    overflow: hidden;
  }
  .brochure-art { position: absolute; inset: 0; }
  .panel { position: absolute; top: 0; height: 811px; width: 380px; }
  .panel--services { left: 0; }
  .panel--contact {
    left: 380px;
    background: linear-gradient(90deg, var(--fold) 0%, #f4f4f5 18%, var(--white) 45%, var(--white) 80%, #ededee 100%);
  }
  .panel--cover { left: 760px; }

  /* Services */
  .services-title {
    position: absolute; left: 31px; top: 254px;
    color: var(--teal); font-weight: 400; font-size: 24px; line-height: 33px;
  }
  .services-list {
    position: absolute; left: 31px; top: 338px; list-style: none;
    font-size: 15.5px; font-weight: 300; color: var(--ink);
  }
  .services-list li { height: 30.5px; line-height: 30.5px; padding-left: 24px; position: relative; white-space: nowrap; }
  .services-list li::before {
    content: ""; position: absolute; left: 0; top: 12px;
    width: 8px; height: 8px; border-radius: 50%; background: var(--teal);
  }
  .services-list li.more::before { display: none; }

  /* Contact */
  .contact-inner { position: absolute; left: 0; width: 380px; text-align: center; }
  .start-title { top: 30px; color: var(--blue); font-size: 28px; font-weight: 400; }
  .start-text {
    position: absolute; left: 36px; top: 78px; width: 310px;
    font-size: 12.5px; line-height: 15px; font-weight: 300; color: var(--ink-dark); text-align: left;
  }
  .schedule { top: 168px; font-size: 24px; line-height: 31px; font-weight: 300; color: var(--ink-dark); }
  .schedule-phone { top: 232px; font-size: 36px; color: var(--blue); font-weight: 400; }
  .hours-title { top: 298px; font-size: 29px; color: var(--teal); font-weight: 400; }
  .hours-text { top: 337px; font-size: 23px; line-height: 32px; font-weight: 300; color: var(--ink-dark); }

  .brand { position: absolute; display: flex; align-items: center; gap: 10px; }
  .brand-name { color: var(--ink); font-weight: 400; white-space: nowrap; }
  .brand-dot { border-radius: 50%; background: var(--teal-soft); }
  .brand--small { left: 22px; top: 634px; }
  .brand--small .brand-name { font-size: 22px; }
  .brand--small .brand-dot { width: 26px; height: 26px; }
  .address {
    position: absolute; left: 22px; top: 702px;
    font-size: 13.5px; line-height: 20px; font-weight: 300; color: var(--ink-dark); font-style: normal;
  }

  /* Cover */
  .brand--large { left: 50px; top: 92px; }
  .brand--large .brand-name { font-size: 31px; }
  .brand--large .brand-dot { width: 40px; height: 40px; }
  .web {
    position: absolute; left: 0; width: 380px; top: 740px; text-align: center;
    color: var(--white); font-size: 19px; letter-spacing: 2.4px; font-weight: 400;
  }
</style>
</head>
<body>
<main class="brochure">
  <svg class="brochure-art" width="1140" height="811" viewBox="0 0 1140 811">
    <defs>
      <linearGradient id="kids-group-tone" x1="0" y1="0" x2="0" y2="1">
        <stop offset="0" stop-color="#eef3f6"/>
        <stop offset="0.6" stop-color="#e9b98f"/>
        <stop offset="1" stop-color="#7fb8d8"/>
      </linearGradient>
      <linearGradient id="classroom-tone" x1="0" y1="0" x2="1" y2="1">
        <stop offset="0" stop-color="#a9cde2"/>
        <stop offset="0.5" stop-color="#e6b3a4"/>
        <stop offset="1" stop-color="#d9dde3"/>
      </linearGradient>
    </defs>
    <!-- Services panel photo -->
    <path role="img" aria-label="Photo of a group of cheerful schoolchildren raising their arms"
          d="M0,0 H380 V250 Q210,192 0,212 Z" fill="url(#kids-group-tone)"/>
    <path d="M0,222 Q210,200 380,260" fill="none" stroke="var(--blue)" stroke-width="9"/>
    <!-- Cover blue sweep -->
    <circle cx="948" cy="870" r="290" fill="var(--blue)"/>
    <!-- Cover photo frame -->
    <circle cx="926" cy="442" r="236" fill="var(--teal)"/>
    <circle cx="932" cy="446" r="226" fill="var(--white)"/>
    <circle role="img" aria-label="Photo of a smiling girl sitting at a classroom desk with classmates behind her"
            cx="934" cy="448" r="216" fill="url(#classroom-tone)"/>
  </svg>

  <section class="panel panel--services">
    <h2 class="services-title">Services<br>Offered for Your Child</h2>
    <ul class="services-list">
      <li>Social Skills</li>
      <li>Oral Motor</li>
      <li>Sensory Activities</li>
      <li>Feeding</li>
      <li>Handling Techniques</li>
      <li>Handwriting</li>
      <li>Home Exercise Program</li>
      <li>Kinesiotaping</li>
      <li>Guided Listening Program (GLP)</li>
      <li>Neuro-Developmental Treatment</li>
      <li>Patient/Parent Education</li>
      <li>Postural Reeducation</li>
      <li>Sensory Integration</li>
      <li>Therapeutic play</li>
      <li class="more">…and much more!</li>
    </ul>
  </section>

  <section class="panel panel--contact">
    <h2 class="contact-inner start-title">How to get started!</h2>
    <p class="start-text">If you or someone you know has concerns about their child’s development, discuss with your doctor the concern and request a prescription for an occupational therapy evaluation.</p>
    <p class="contact-inner schedule">To schedule<br>an appointment, call</p>
    <p class="contact-inner schedule-phone">(555) 014-2290</p>
    <h3 class="contact-inner hours-title">Business Hours</h3>
    <p class="contact-inner hours-text">Monday-Saturday<br>8:00am-7:00pm</p>
    <div class="brand brand--small">
      <span class="brand-name">Kite Kids Therapy</span>
      <span class="brand-dot"></span>
    </div>
    <address class="address">
      48 Maple Ave, Riverton, Texas 78000<br>
      (555) 014-2290<br>
      hello@kitekidstherapy.com
    </address>
  </section>

  <section class="panel panel--cover">
    <div class="brand brand--large">
      <span class="brand-name">Kite Kids Therapy</span>
      <span class="brand-dot"></span>
    </div>
    <p class="web">www.kitekidstherapy.com</p>
  </section>
</main>
</body>
</html>
```